Mental Health care Company in Washington DC

We are a new mental health care services provider in Washington DC. Please look at these sites.
https://marlowbrookpartners.com
https://www.quillstoneinc.com
https://velmarsh-kt.org/
https://www.trivanqx.com
https://www.thelanternofqz.com

```html
<!DOCTYPE html>
<html lang="en">
<head>
<meta charset="UTF-8">
<title>Lumen Harbor Health – Mental Health Care in Washington DC</title>
<link href="https://fonts.googleapis.com/css2?family=Poppins:wght@400;500;600;700&display=swap" rel="stylesheet">
<style>
:root{
  --orange:#f47b20;
  --navy:#1c2541;
  --ink:#222a3a;
  --muted:#5d6473;
  --teal:#5cc3c0;
  --teal-soft:#bfe9e6;
  --grey-bg:#f1f1f3;
  --brown:#4a2411;
  --white:#ffffff;
}
*{box-sizing:border-box;margin:0;padding:0}
html,body{width:1200px;height:4212px;overflow:hidden}
body{font-family:"Poppins",sans-serif;color:var(--ink);background:var(--white);font-size:15px;line-height:1.6;position:relative}
.btn{display:inline-block;background:var(--orange);color:var(--white);font-size:14px;font-weight:500;padding:10px 26px;border-radius:6px;text-decoration:none;white-space:nowrap}
.btn.sm{font-size:12px;padding:6px 18px;border-radius:5px}
.tag{display:flex;align-items:center;gap:10px;font-size:15px;color:var(--ink)}
.tag .sq{width:26px;height:26px;background:var(--teal-soft);border-radius:3px;display:flex;align-items:center;justify-content:center}
.tag .sq i{width:12px;height:12px;background:var(--teal);display:block;border-radius:2px}
.ph{display:block}
/* top bar */
.topbar{height:40px;background:#2b2b2b;color:#e6e6e6;font-size:13px;display:flex;align-items:center;padding:0 112px}
.topbar .right{margin-left:auto;display:flex;gap:40px}
.topbar span{display:flex;align-items:center;gap:8px}
/* nav */
.nav{height:110px;display:flex;align-items:center;padding:0 112px}
.logo{display:flex;align-items:center;gap:10px;font-weight:700;font-size:22px;color:var(--navy)}
.logo i{width:16px;height:16px;background:var(--orange);border-radius:50%;display:block}
.nav ul{list-style:none;display:flex;gap:30px;margin-left:auto;margin-right:40px;font-size:14px;font-weight:500}
.nav li.active{color:var(--orange)}
/* hero */
.hero{position:relative;height:550px;background:linear-gradient(90deg,#1a1612 0%,#3a2b1f 45%,#9c6a3a 75%,#e3b072 100%);color:var(--white);padding:110px 112px 0}
.hero h1{font-size:44px;line-height:1.25;font-weight:600;width:520px}
.hero p{font-size:17px;width:470px;margin:22px 0 28px}
.hero .row{display:flex;align-items:center;gap:30px}
.avatars{display:flex;align-items:center;gap:12px;font-size:13px}
.avatars .dots{display:flex}
.avatars .dots i{width:34px;height:34px;border-radius:50%;background:#b89478;border:2px solid var(--white);margin-left:-10px;display:block}
.avatars .dots i:first-child{margin-left:0}
.stars{color:#f8b73a;letter-spacing:2px;font-size:13px}
/* about */
.about{display:flex;padding:130px 112px 0;gap:50px;height:450px}
.about .pics{display:grid;grid-template-columns:232px 210px;grid-template-rows:150px 150px;gap:20px;width:460px}
.about .pics .tall{grid-row:span 2;border-radius:10px;background:linear-gradient(160deg,#d9d2cb,#8a8582)}
.about .pics .a{border-radius:10px;background:linear-gradient(160deg,#f1ece7,#a89c92)}
.about .pics .b{border-radius:10px;background:linear-gradient(160deg,#c9c2ba,#5d524b)}
.about .text{padding-top:20px;width:490px}
.about h2{font-size:34px;line-height:1.25;font-weight:600;margin:12px 0 14px}
.about h2 em{font-style:normal;color:var(--orange)}
.about .text p{color:var(--muted);font-size:14px;padding-bottom:14px;border-bottom:1px solid #d6d6d6;margin-bottom:24px}
.about .cta{display:flex;align-items:center;gap:40px;font-weight:500}
.about .cta span{display:flex;align-items:center;gap:12px;white-space:nowrap}
/* services */
.services{background:var(--grey-bg);margin-top:100px;height:930px;padding:80px 112px 0;position:relative}
.services .intro{position:absolute;left:112px;top:140px;width:290px}
.services h2{font-size:34px;line-height:1.3;font-weight:600;margin:12px 0 14px}
.services h2 em{font-style:normal;color:var(--orange)}
.services .intro p{font-size:14px;color:var(--muted);margin-bottom:24px}
.card{position:absolute;width:300px;height:340px;background:var(--white);border-radius:8px;box-shadow:0 4px 14px rgba(0,0,0,.1);text-align:center;overflow:hidden}
.card .img{height:180px;margin:10px 10px 0;border-radius:6px}
.card h3{font-size:16px;font-weight:600;margin:18px 0 8px}
.card p{font-size:12px;color:var(--muted);padding:0 30px;line-height:1.55;margin-bottom:14px}
.c1{left:450px;top:130px}.c2{left:780px;top:130px}
.c3{left:112px;top:520px}.c4{left:450px;top:520px}.c5{left:780px;top:520px}
.g1{background:linear-gradient(160deg,#dfe3e6,#8c9096)}
.g2{background:linear-gradient(160deg,#e4d6c6,#7d6a58)}
.g3{background:linear-gradient(160deg,#d6b58f,#6e4c33)}
.g4{background:linear-gradient(160deg,#8a98a8,#3a4452)}
.g5{background:linear-gradient(160deg,#c9d2da,#6b6360)}
/* value */
.value{position:relative;height:570px;margin-top:80px;background:linear-gradient(90deg,#3c3a3a 0%,#6f6e6b 40%,#5a4a3e 70%,#2d2420 100%)}
.value .panel{position:absolute;left:205px;top:115px;width:790px;height:320px;background:rgba(120,205,205,.62);border-radius:10px;text-align:center;color:var(--white);padding-top:50px}
.value .tag{justify-content:center;color:var(--white)}
.value h2{font-size:34px;font-weight:600;margin:8px 0 10px}
.value p{font-size:14px;width:480px;margin:0 auto 26px}
/* blog */
.blog{height:600px;padding-top:65px;text-align:center}
.blog .tag{justify-content:center}
.blog h2{font-size:34px;font-weight:600;margin:10px 0 40px}
.posts{display:flex;gap:30px;justify-content:center}
.post{width:310px;position:relative}
.post .img{height:140px;border-radius:8px 8px 0 0}
.post .body{background:var(--white);margin:-20px 20px 0;position:relative;border-radius:6px;box-shadow:0 4px 14px rgba(0,0,0,.1);padding:22px 16px 18px}
.post .date{position:absolute;top:-14px;left:50%;transform:translateX(-50%);background:var(--white);font-size:12px;padding:3px 14px;border-radius:4px;box-shadow:0 2px 6px rgba(0,0,0,.1);display:flex;gap:6px;align-items:center;white-space:nowrap}
.post h3{font-size:14px;font-weight:600;line-height:1.4;margin-bottom:12px}
/* cta */
.reach{margin:0 112px;height:290px;border-radius:10px;overflow:hidden;display:flex;background:linear-gradient(90deg,#e8f4f4,#8fd6d3)}
.reach .img{width:460px;background:linear-gradient(160deg,#c9c6c0,#6c655d)}
.reach .text{padding:55px 0 0 40px}
.reach h2{font-size:34px;font-weight:600;margin:8px 0 8px}
.reach p{font-size:14px;color:var(--muted);width:380px;margin-bottom:24px}
/* footer */
.footer{position:absolute;top:3830px;left:0;width:1200px;height:382px;background:var(--brown);color:#f1e6de;padding:70px 112px 0}
.fcols{display:flex}
.fbrand{width:300px}
.fbrand .logo{color:var(--white);font-size:22px}
.fbrand p{font-size:14px;margin:14px 0 14px;width:200px}
.social{display:flex;gap:12px}
.social i{width:18px;height:18px;border:2px solid #f1e6de;border-radius:50%;display:block}
.fcol{width:220px}
.fcol.contact{width:256px}
.fcol h4{font-size:20px;font-weight:600;color:var(--white);margin-bottom:14px}
.fcol li{list-style:none;font-size:14px;margin-bottom:8px;display:flex;gap:8px;align-items:flex-start;white-space:nowrap}
.copy{position:absolute;left:112px;right:112px;bottom:0;height:80px;border-top:1px solid rgba(255,255,255,.25);display:flex;align-items:center;justify-content:center;font-size:13px}
</style>
</head>
<body>

<div class="topbar">
  <span><svg width="14" height="14" viewBox="0 0 24 24" fill="none" stroke="#e6e6e6" stroke-width="2"><circle cx="12" cy="12" r="9"/><path d="M12 7v5l3 2"/></svg>Monday - Friday: 9 AM - 6 PM</span>
  <div class="right">
    <span><svg width="14" height="14" viewBox="0 0 24 24" fill="#e6e6e6"><path d="M6.6 10.8a15 15 0 006.6 6.6l2.2-2.2a1 1 0 011-.24 11.4 11.4 0 003.6.58 1 1 0 011 1V20a1 1 0 01-1 1A17 17 0 013 4a1 1 0 011-1h3.5a1 1 0 011 1c0 1.25.2 2.45.57 3.57a1 1 0 01-.25 1z"/></svg>+1 202 555 0147</span>
    <span><svg width="14" height="14" viewBox="0 0 24 24" fill="none" stroke="#e6e6e6" stroke-width="2"><rect x="3" y="5" width="18" height="14" rx="2"/><path d="M3 7l9 6 9-6"/></svg>info@lumenharborhealth.com</span>
  </div>
</div>

<nav class="nav">
  <div class="logo"><i></i>Lumen Harbor</div>
  <ul><li class="active">Home</li><li>About</li><li>Services</li><li>Blog</li><li>Contact Us</li></ul>
  <a class="btn" href="#">Schedule an Appointment</a>
</nav>

<section class="hero">
  <h1>Compassionate Mental Health Care in Washington DC</h1>
  <p>Empowering individuals and families through personalized, holistic behavioral health services.</p>
  <div class="row">
    <a class="btn" href="#">Schedule an Appointment</a>
    <div class="avatars">
      <div class="dots" role="img" aria-label="Small portraits of clients"><i></i><i></i><i></i><i></i></div>
      <div><div class="stars">★★★★★</div>1000+ People have been helped</div>
    </div>
  </div>
</section>

<section class="about">
  <div class="pics">
    <div class="ph tall" role="img" aria-label="Client talking with a therapist"></div>
    <div class="ph a" role="img" aria-label="Smiling counselor"></div>
    <div class="ph b" role="img" aria-label="Therapist taking notes"></div>
  </div>
  <div class="text">
    <div class="tag"><span class="sq"><i></i></span>About Us</div>
    <h2>Dedicated to Transform your <em>Mental Health</em></h2>
    <p>Lorem ipsum dolor sit amet, consectetur adipiscing elit, sed do eiusmod tempor incididunt ut labore et dolore magna aliqua.</p>
    <div class="cta">
      <a class="btn" href="#">Discover More</a>
      <span><svg width="22" height="22" viewBox="0 0 24 24" fill="#222a3a"><path d="M6.6 10.8a15 15 0 006.6 6.6l2.2-2.2a1 1 0 011-.24 11.4 11.4 0 003.6.58 1 1 0 011 1V20a1 1 0 01-1 1A17 17 0 013 4a1 1 0 011-1h3.5a1 1 0 011 1c0 1.25.2 2.45.57 3.57a1 1 0 01-.25 1z"/></svg>+1 (202) 555 0199</span>
    </div>
  </div>
</section>

<section class="services">
  <div class="intro">
    <div class="tag"><span class="sq"><i></i></span>What we do</div>
    <h2>Comprehensive Mental Health <em>Assessments</em></h2>
    <p>Lorem ipsum dolor sit amet, consectetur adipiscing elit.</p>
    <a class="btn" href="#">See More Services</a>
  </div>
  <div class="card c1"><div class="img g1" role="img" aria-label="Mental health evaluation session"></div><h3>Mental Health Evaluations</h3><p>Lorem ipsum dolor sit amet, consectetur adipiscing elit. Ut elit tellus, luctus nec</p><a class="btn sm" href="#">Learn More</a></div>
  <div class="card c2"><div class="img g2" role="img" aria-label="Psychological assessment meeting"></div><h3>Psychological Assessment</h3><p>Lorem ipsum dolor sit amet, consectetur adipiscing elit. Ut elit tellus, luctus nec</p><a class="btn sm" href="#">Learn More</a></div>
  <div class="card c3"><div class="img g3" role="img" aria-label="In-depth testing with a counselor"></div><h3>In-depth Testing</h3><p>Lorem ipsum dolor sit amet, consectetur adipiscing elit. Ut elit tellus, luctus nec</p><a class="btn sm" href="#">Learn More</a></div>
  <div class="card c4"><div class="img g4" role="img" aria-label="Person coping with anxiety"></div><h3>Depression &amp; Anxiety</h3><p>Lorem ipsum dolor sit amet, consectetur adipiscing elit. Ut elit tellus, luctus nec</p><a class="btn sm" href="#">Learn More</a></div>
  <div class="card c5"><div class="img g5" role="img" aria-label="Youth session with a counselor"></div><h3>Youth Assessments</h3><p>Lorem ipsum dolor sit amet, consectetur adipiscing elit. Ut elit tellus, luctus nec</p><a class="btn sm" href="#">Learn More</a></div>
</section>

<section class="value" role="img" aria-label="Therapy session in a warm office">
  <div class="panel">
    <div class="tag"><span class="sq"><i></i></span>Our Value</div>
    <h2>Building A Better Health Care System</h2>
    <p>Lorem ipsum dolor sit amet, consectetur adipiscing elit, sed do eiusmod tempor incididunt ut labore et dolore magna aliqua.</p>
    <a class="btn" href="#">Discover More</a>
  </div>
</section>

<section class="blog">
  <div class="tag"><span class="sq"><i></i></span>Our Blog</div>
  <h2>Healthy Mind, Healthy Life</h2>
  <div class="posts">
    <article class="post"><div class="img g1" role="img" aria-label="Group conversation"></div><div class="body"><span class="date">▦ May 01,2023</span><h3>10 Simple Habits to Boost Your Mental Health Every Day</h3><a class="btn sm" href="#">Read More</a></div></article>
    <article class="post"><div class="img g2" role="img" aria-label="Counseling session"></div><div class="body"><span class="date">▦ May 01,2023</span><h3>How to Recognize and Manage Anxiety: Expert Tips</h3><a class="btn sm" href="#">Read More</a></div></article>
    <article class="post"><div class="img g5" role="img" aria-label="Support group meeting"></div><div class="body"><span class="date">▦ May 01,2023</span><h3>Breaking the Stigma: Why Seeking Therapy is a Strength</h3><a class="btn sm" href="#">Read More</a></div></article>
  </div>
</section>

<section class="reach">
  <div class="img" role="img" aria-label="Two people talking in a bright room"></div>
  <div class="text">
    <div class="tag"><span class="sq"><i></i></span>Start Today</div>
    <h2>Reach Out for Support</h2>
    <p>Lorem ipsum dolor sit amet, consectetur adipiscing elit, sed do eiusmod tempor incididunt.</p>
    <a class="btn" href="#">Schedule an Appointment</a>
  </div>
</section>

<footer class="footer">
  <div class="fcols">
    <div class="fbrand">
      <div class="logo"><i></i>Lumen Harbor</div>
      <p>Compassionate Mental Health Care in Washington DC</p>
      <div class="social"><i></i><i></i><i></i><i></i><i></i></div>
    </div>
    <div class="fcol"><h4>Services</h4><ul><li>Medical Services</li><li>Behavioral Health</li><li>Human Services</li><li>Spiritual Needs</li></ul></div>
    <div class="fcol"><h4>Quick Links</h4><ul><li>Home</li><li>About</li><li>Services</li><li>Contact</li></ul></div>
    <div class="fcol contact"><h4>Contact Us</h4><ul><li>☏ +1 202 555 0147</li><li>✉ info@lumenharborhealth.com</li><li>◷ Monday - Friday<br>9 AM - 6 PM</li></ul></div>
  </div>
  <div class="copy">© 2025, Lumen Harbor Health. All rights reserved.</div>
</footer>

</body>
</html>
```